E-commerce Website needs category banner

What we need for our category banner is a clean, predominately black design that showcases the product we are trying to sell (currently only 1), and a few subtle gradients that follow the pattern set by previous designs.

An example will be provided to showcase what we want.

It needs to say:
Outdoor Motion Detection Lighting in large, clear font similar to the example provided.
Updates

Please ensure dimensions are as follows: 980x300

Target Market(s)

Senior citizens, businesses, homeowners, families, etc

Industry/Entity Type

Product

Font styles to use
Sans Serif

Requirements
Must have
• It needs to say:
Outdoor Motion Detection Lighting in large, clear font similar to the example provided
980x300 is the required size!
Should not have
• Too much going on- clean and simple please (no crazy fonts, logos, etc)

```html
<!DOCTYPE html>
<html lang="en">
<head>
<meta charset="utf-8">
<title>Outdoor Motion Detection Lighting – Category Banner</title>
<link href="https://fonts.googleapis.com/css2?family=Nunito+Sans:wght@300;800&display=swap" rel="stylesheet">
<style>
  :root {
    --bg-dark: #262626;
    --bg-mid: #454545;
    --bg-light: #7a7a7a;
    --text: #ffffff;
    --product-light: #f4f4f4;
    --product-mid: #dcdcdc;
    --product-shade: #b4b4b4;
  }
  html, body {
    margin: 0;
    padding: 0;
    width: 1200px;
    height: 465px;
    overflow: hidden;
    background: var(--bg-dark);
  }
  .banner {
    position: relative;
    width: 1200px;
    height: 465px;
    overflow: hidden;
    background:
      radial-gradient(ellipse 620px 420px at 1000px 430px, rgba(122,122,122,0.85) 0%, rgba(122,122,122,0) 75%),
      linear-gradient(100deg, var(--bg-dark) 0%, var(--bg-mid) 50%, #5e5e5e 100%);
    font-family: "Nunito Sans", Arial, sans-serif;
    color: var(--text);
  }
  .headline {
    position: absolute;
    left: 110px;
    width: 600px;
    margin: 0;
    text-align: center;
    line-height: 1;
    white-space: nowrap;
  }
  .headline--lead {
    top: 93px;
    font-size: 62px;
    font-weight: 300;
  }
  .headline--main {
    font-size: 90px;
    font-weight: 800;
    letter-spacing: 1px;
  }
  .headline--line1 { top: 166px; }
  .headline--line2 { top: 264px; }
  .product-shot {
    position: absolute;
    left: 790px;
    top: 66px;
    width: 368px;
    height: 340px;
  }
</style>
</head>
<body>
  <main class="banner">
    <h1 class="headline headline--lead">Outdoor Motion</h1>
    <p class="headline headline--main headline--line1">DETECTION</p>
    <p class="headline headline--main headline--line2">LIGHTING</p>
    <svg class="product-shot" viewBox="0 0 368 340" role="img" aria-label="Product photo: two white wall-mounted battery motion sensor spotlights with LED lamps and swivel mounts">
      <defs>
        <linearGradient id="productFill" x1="0" y1="0" x2="1" y2="1">
          <stop offset="0%" stop-color="var(--product-light)"/>
          <stop offset="55%" stop-color="var(--product-mid)"/>
          <stop offset="100%" stop-color="var(--product-shade)"/>
        </linearGradient>
      </defs>
      <rect x="0" y="0" width="368" height="340" rx="28" fill="url(#productFill)"/>
    </svg>
  </main>
</body>
</html>
```